“Professional 9x12 Pocket Folder Design – Roofing, Siding, Windows, Doors, Decks, Solar

✅ Page 1: Front Cover (Main Visual Impact)

Goal: Strong visual first impression representing all services Delmo’s Roofing offers.

Design Instructions:
• Top: Big, bold headline with Delmo’s Roofing (or company logo).
• Center: A high-quality image of a beautiful home that clearly shows:
• New roof (preferably dark shingles)
• Modern black-trim windows
• Upgraded front door
• Stylish siding (horizontal or board & batten)
• Visible garage door
• Optional: solar panels on the roof
• Optional: small composite front porch or deck
• Bottom Section (beneath the house image): Add keywords like:
Roofing • Siding • Windows • Doors • Decks • Solar • Local & Trusted

⸻

✅ Page 2: Back Cover

Goal: Tell the story of the company + display contact information for offices.

Design Instructions:
• Top Half: Section titled:
Our Story or About Delmo’s Roofing

Suggested Text (can be customized):
With over two decades of dedication to quality craftsmanship, Delmo’s Roofing has grown from a small local team into one of the region’s most trusted names in exterior home improvement. Our mission is to bring lasting beauty, energy efficiency, and protection to every home we touch.
• Bottom Half: Title:
Our Offices

Include up to 4 office addresses

Delmo's Roofing
2741 Fennimore St.
Stoughton, MA 02072
Delmo's Roofing
3382 Halbrook Ave, Warwick, RI 02888
Delmo's Roofing
917 E Tamsin St, Middleborough, MA 02346
Delmo's Roofing
4126 Pelliton Hwy, East Wareham, MA 02538 ( Showroom )

⸻

✅ Inside Pockets

🔹 Left Pocket:

Title:

We’d Love Your Feedback

Text Suggestion:

Enjoyed your experience? Please leave us a review. Your feedback helps us grow and serve others better.

Add a QR code linking to the review page.for quillro reviews

🔹 Right Pocket:

Your Product Specialist
Kasim Holter
📞 B:781-555-0193
P:774-555-0147
✉️ kholter@delmosroofing-example.com

Let this info be printed/stamped directly on the folder, not using business cards
Our website https://delmosroofing-example.com/?sfw=pass1751118580#

Feel free to take pictures from the website and use anything that is needed .

If we can add a flyer extra I’ll be willing to pay for that separate .
✅ Flyer Insert #1 (Double-Sided)

🔹 SIDE A: “Before & After Showcase”
• 4 Sections (lined up cleanly):
• Roofing
• Windows
• Skylights
• Decks
Each section includes:
• 📸 Before / After photo
• ✍️ Small description of the job (town + result)

🔹 SIDE B: “The Project Journey”

“What to Expect When You Work with Kasim”

• Step 1: Free Home Visit & Consultation
• Step 2: Custom Design Solutions
• Step 3: Quality Installation by Experts
• Step 4: Final Walkthrough + Satisfaction Check
• Soft closing line

Please use our best before and after pictures and take the data from Delmosroofing-example.com

```html
<!DOCTYPE html>
<html lang="en">
<head>
<meta charset="utf-8">
<title>Delmo's Roofing – Flyer Insert</title>
<link rel="stylesheet" href="https://fonts.googleapis.com/css2?family=Figtree:wght@300;400;600;700;800&display=swap">
<style>
:root{
  --blue:#0b62a8;
  --gold:#bf9a4f;
  --row:#c9d6ec;
  --ink:#2a2a2a;
  --stage:#c9c8c6;
  --shingle:#4a5049;
  --white:#fff;
}
*{box-sizing:border-box;margin:0;padding:0}
html,body{width:1200px;height:796px;overflow:hidden}
body{background:var(--stage);font-family:"Figtree",Arial,sans-serif;color:var(--ink);position:relative}
.sheet{position:absolute;top:63px;width:523px;height:677px;overflow:hidden}
.sheet--showcase{left:69px;background:var(--white)}
.sheet--journey{left:622px;background:var(--shingle)}
.abs{position:absolute}

.brand-mark{display:flex;align-items:center;justify-content:center;gap:5px;text-align:center;
  font-weight:800;color:var(--blue);font-size:19px;line-height:1.05;background:var(--white)}
.brand-mark__dot{width:9px;height:9px;background:var(--gold);flex:none}

.headline{left:211px;top:18px;line-height:1}
.headline__lead{font-size:40px;font-weight:400;color:var(--gold);letter-spacing:.5px}
.headline__main{font-size:41px;font-weight:700;color:var(--blue);margin-top:-1px}

.divider{background:#1c1c1c}
.case{position:absolute;width:232px}
.case__title{font-size:18px;color:var(--blue);font-weight:400;line-height:1}
.case__sub{font-size:11.5px;margin-top:8px;line-height:1}
.specs{width:100%;border-collapse:collapse;margin-top:7px;table-layout:fixed}
.specs th{background:var(--gold);color:var(--white);font-size:7px;font-weight:700;height:12px;border-right:1px solid var(--white)}
.specs td{background:var(--row);font-size:7.5px;text-align:center;height:13px;border-right:1px solid var(--white);border-top:1px solid var(--white)}
.specs th:last-child,.specs td:last-child{border-right:none}
.notes{display:flex;gap:11px;margin-top:6px;font-size:6.3px;line-height:1.3}
.notes div{flex:1}
.notes b{display:block;color:var(--blue);font-size:6.6px;font-weight:700}
.photo{position:absolute;height:75px}
.photo--roof{background:linear-gradient(160deg,#7c8a7a,#50606d 55%,#3f4a36)}
.photo--roof2{background:linear-gradient(160deg,#9aa0a4,#c9ced4 50%,#6e6a5c)}
.photo--win{background:linear-gradient(170deg,#cbc7b8,#a9a392 60%,#5a5a55)}
.photo--win2{background:linear-gradient(170deg,#2d5fb8,#cfcabb 45%,#4a4a48)}
.photo--sky{background:linear-gradient(175deg,#4d7dcc,#2d3b55 50%,#4b7a2f)}
.photo--sky2{background:linear-gradient(175deg,#4d86d6,#e8ecee 45%,#5c9a36)}
.photo--deck{background:linear-gradient(160deg,#c2c8cf,#c8763a 60%,#8b4a22)}
.photo--deck2{background:linear-gradient(160deg,#d7c99a,#e8e4de 40%,#6d4a40)}
.tag{position:absolute;font-size:12px;line-height:1}

.closing{left:0;top:580px;width:523px;height:97px;border-top:8px solid var(--gold);background:var(--blue);color:var(--white);text-align:center;padding-top:11px}
.closing__lead{font-size:22px;font-weight:700;line-height:1.2}
.closing__tail{font-size:22px;font-weight:300;line-height:1.35;letter-spacing:.4px}

.journey-panel{left:28px;top:67px;width:464px;height:575px;background:var(--white);border:2px solid var(--gold)}
.journey-title{left:0;width:523px;top:112px;text-align:center;font-size:39px;color:var(--blue);font-weight:400;line-height:1;letter-spacing:.3px}
.journey-title b{font-weight:800}
.journey-sub{left:0;width:523px;top:160px;text-align:center;font-size:16px;line-height:1}
.step{position:absolute;width:126px;height:67px;border:1.5px solid var(--blue);background:var(--white);text-align:center;padding-top:5px}
.step__num{font-size:28px;color:var(--gold);line-height:1}
.step__text{font-size:8px;font-weight:700;line-height:1.3;margin-top:3px;color:#1d1d1d}
.flow{left:0;top:0}

.specialist{left:61px;top:533px;width:223px;height:144px;background:var(--blue);color:var(--white)}
.specialist__head{height:37px;background:var(--gold);font-size:14px;font-weight:700;display:flex;align-items:center;justify-content:center}
.specialist__body{padding:7px 0 0 34px;font-size:11px;line-height:14.3px}
.specialist__name{font-weight:700;font-size:11.5px}
.specialist__line{display:flex;align-items:center;gap:4px;white-space:nowrap}
.specialist__line--small{font-size:9.5px}
.icon{width:8px;height:8px;border-radius:50%;background:var(--gold);flex:none}
</style>
</head>
<body>

<section class="sheet sheet--showcase">
  <div class="abs brand-mark" style="left:22px;top:13px;width:142px;height:76px"><span class="brand-mark__dot"></span><span>Delmo's Roofing</span></div>
  <h1 class="abs headline"><div class="headline__lead">Satisfied</div><div class="headline__main">Home owners</div></h1>

  <div class="abs divider" style="left:260px;top:106px;width:3px;height:463px"></div>
  <div class="abs divider" style="left:20px;top:337px;width:483px;height:3px"></div>

  <article class="case" style="left:21px;top:104px">
    <h2 class="case__title">Roofing</h2>
    <p class="case__sub">Roof Installation Wareham, MA</p>
    <table class="specs"><colgroup><col style="width:27%"><col style="width:29%"><col style="width:44%"></colgroup>
      <tr><th>Location:</th><th>Services:</th><th>Materials:</th></tr>
      <tr><td>Wareham</td><td>Roofing</td><td>Crestline Northwood</td></tr></table>
    <div class="notes"><div><b>The Problem</b>Many leaks and damage from years of wear and tear</div>
      <div><b>The Solution</b>Stellarock Northwood Pale Ash's exceptional durability and beauty. The outcome was a gorgeously restored roof and the homeowner's peace of mind</div></div>
  </article>
  <div class="photo photo--roof" style="left:21px;top:237px;width:113px" role="img" aria-label="Before photo: aerial view of worn roof in Wareham"></div>
  <div class="photo photo--roof2" style="left:140px;top:237px;width:113px" role="img" aria-label="After photo: aerial view of new grey shingle roof"></div>
  <span class="tag" style="left:21px;top:315px">Before</span><span class="tag" style="left:140px;top:315px">After</span>

  <article class="case" style="left:272px;top:104px">
    <h2 class="case__title">Windows</h2>
    <p class="case__sub">Window Replacement Sharon, MA</p>
    <table class="specs"><colgroup><col style="width:28%"><col style="width:31%"><col style="width:41%"></colgroup>
      <tr><th>Location:</th><th>Services:</th><th>Materials:</th></tr>
      <tr><td>Sharon</td><td>Windows</td><td>Halden / White</td></tr></table>
    <div class="notes"><div><b>The Problem</b>The previous windows were outdated windows with very low visibility. The window frame was deteriorated with cracks that let in moister and cold air.</div>
      <div><b>The Solution</b>Replaced with fiberglass mesh screens on vented windows with no grids. Replacing the windows saved the homeowner not only a headache but also on their utility bills.</div></div>
  </article>
  <div class="photo photo--win" style="left:272px;top:242px;width:106px;height:71px" role="img" aria-label="Before photo: old arched windows on beige siding"></div>
  <div class="photo photo--win2" style="left:384px;top:242px;width:119px;height:71px" role="img" aria-label="After photo: new white arched windows under blue sky"></div>
  <span class="tag" style="left:272px;top:315px">Before</span><span class="tag" style="left:384px;top:315px">After</span>

  <article class="case" style="left:20px;top:349px">
    <h2 class="case__title">Skylights</h2>
    <p class="case__sub">Skylight Install in Canton</p>
    <table class="specs"><colgroup><col style="width:29.5%"><col style="width:34.5%"><col style="width:36%"></colgroup>
      <tr><th>Location:</th><th>Services:</th><th>Materials:</th></tr>
      <tr><td>Canton</td><td>Skylights</td><td>Lumavent</td></tr></table>
    <div class="notes"><div><b>The Solution</b>We are proud to be a certified installer of LUMAVENT skylights. For over sixty years, LUMAVENT has been a leader in skylight and roof light solutions. We are one of Lumavent's leading installers in the area. Whether you are getting your roof replaced and want a skylight installed or if you have a newer roof and just need some more natural light, we are the team for you!</div></div>
  </article>
  <div class="photo photo--sky" style="left:20px;top:482px;width:113px" role="img" aria-label="Before photo: cape house with dark roof in Canton"></div>
  <div class="photo photo--sky2" style="left:140px;top:482px;width:113px" role="img" aria-label="After photo: white cape house with new skylights"></div>
  <span class="tag" style="left:20px;top:561px">Before</span><span class="tag" style="left:140px;top:561px">After</span>

  <article class="case" style="left:271px;top:349px">
    <h2 class="case__title">Decks</h2>
    <p class="case__sub">Deck Installation in Stoughton, MA</p>
    <table class="specs"><colgroup><col style="width:67%"><col style="width:33%"></colgroup>
      <tr><th>Location:</th><th>Services:</th></tr>
      <tr><td>Stoughton, MA <span style="font-size:6px">and its surrounding area</span></td><td>Roofing</td></tr></table>
    <div class="notes"><div><b>The Solution</b>We are proud to offer decking replacement, and installation to homeowners. When you want a local and trusted contractor that is guaranteed to get the job done right, look no further than our decking team here at Delmo's!</div></div>
  </article>
  <div class="photo photo--deck" style="left:272px;top:480px;width:112px;height:78px" role="img" aria-label="Before photo: old wooden deck with white railing"></div>
  <div class="photo photo--deck2" style="left:391px;top:480px;width:111px;height:78px" role="img" aria-label="After photo: new brown composite deck with white railing"></div>
  <span class="tag" style="left:272px;top:561px">Before</span><span class="tag" style="left:391px;top:561px">After</span>

  <footer class="abs closing">
    <div class="closing__lead">Let's Work Together</div>
    <div class="closing__tail">to Create the Home You Deserve.</div>
  </footer>
</section>

<section class="sheet sheet--journey" role="img" aria-label="Dark grey roof shingle texture background">
  <div class="abs journey-panel"></div>
  <div class="abs brand-mark" style="left:190px;top:31px;width:143px;height:76px;border:2px solid var(--gold)"><span class="brand-mark__dot"></span><span>Delmo's Roofing</span></div>
  <h2 class="abs journey-title">The <b>Project Journey</b></h2>
  <p class="abs journey-sub">What to Expect When You Work with Kasim</p>

  <svg class="abs flow" width="523" height="677" viewBox="0 0 523 677" aria-hidden="true">
    <defs><marker id="head" viewBox="0 0 10 10" refX="9" refY="5" markerWidth="5" markerHeight="6" orient="auto"><path d="M0 0 L10 5 L0 10 L3 5 Z" fill="#1c1c1c"/></marker></defs>
    <g fill="none" stroke="#1c1c1c" stroke-width="2" marker-end="url(#head)">
      <path d="M248 225 H360 V276"/>
      <path d="M292 309 H184 V362"/>
      <path d="M248 394 H360 V447"/>
      <path d="M297 480 H172 V532"/>
    </g>
  </svg>

  <div class="step" style="left:122px;top:197px"><div class="step__num">Step 1:</div><div class="step__text">Free Home Visit<br>&amp; Consultation</div></div>
  <div class="step" style="left:292px;top:277px"><div class="step__num">Step 2:</div><div class="step__text">Custom Design<br>Solutions</div></div>
  <div class="step" style="left:122px;top:363px"><div class="step__num">Step 3:</div><div class="step__text">Quality Installation<br>by Experts</div></div>
  <div class="step" style="left:297px;top:448px"><div class="step__num">Step 4</div><div class="step__text">:Final Walkthrough<br>+ Satisfaction Check</div></div>

  <aside class="abs specialist">
    <div class="specialist__head">Your Product Specialist</div>
    <div class="specialist__body">
      <div class="specialist__name">Kasim Holter</div>
      <div class="specialist__line"><span class="icon"></span>781-555-0193</div>
      <div class="specialist__line"><span class="icon"></span>774-555-0147</div>
      <div class="specialist__line specialist__line--small"><span class="icon"></span>kholter@delmosroofing-example.com</div>
      <div class="specialist__line specialist__line--small"><span class="icon"></span>https://delmosroofing-example.com</div>
    </div>
  </aside>
</section>

</body>
</html>
```